" Elaboramos soluções para que nossos clientes possam alocar adequadamente os recursos disponíveis (tempo, dinheiro, contatos, produtos, imagem, infra) em ações e iniciativas que tragam resultados efetivos e sustentáveis, alinhados aos seus valores, metas e partes interessadas. Desenvolvemos para eles projetos de investimentos, análises estratégicas, estudos de viabilidade, relatórios de avaliação e monitoramento, referências para formulação de políticas públicas, treinamentos, capacitações, reuniões, oficinas e tantos outras soluções. Acreditamos que o empreendedorismo e a inovação são mecanismos com os quais podemos apoiar o desenvolvimento sustentável local e regional. Nossa essência competitiva reside na proximidade e conexão para com todas as partes interessadas, compromisso com valores éticos e morais, inteligência, assertividade, inovação e aprendizado. Buscamos contato com as necessidades dos clientes desde o primeiro momento, garantindo que a construção das soluções respeite processos de diálogo contínuo. As principais características de nossos serviços são: - Informações e conhecimento confiáveis e aplicáveis; - Ações que gerem valores tangíveis e intangíveis positivos, especialmente no tocante à imagem e à confiabilidade; - Acesso a ideias, relacionamentos e oportunidades únicos; - Inovação. Considerados os elementos acima, é preciso destacar que toda a nossa atuação se dá em sintonia e parceria com cada indivíduo envolvido. Assim, consideramos as pessoas como fundamento e objetivo de nossa atuação. "

```html
<!DOCTYPE html>
<html lang="pt-BR">
<head>
<meta charset="utf-8">
<title>Verdalia — Manual de Identidade Visual</title>
<link rel="stylesheet" href="https://fonts.googleapis.com/css2?family=Raleway:wght@300;400;500;600&display=swap">
<style>
  :root{
    --backdrop:#eeeae6;
    --paper:#ffffff;
    --ink:#5a5f66;
    --ink-soft:#9aa0a6;
    --teal:#2f9a9b;
    --teal-pale:#cfe9e8;
    --lilac:#b9a3d4;
    --mint:#cfe8d6;
    --sky:#cfe2ee;
    --rose:#e9d3e6;
    --plum-dark:#3b2a3f;
    --plum:#5a3466;
    --teal-dark:#1f3a3c;
    --violet:#6e4c86;
    --pearl:#f4f4f6;
    --green-light:#c9e4b5;
    --grey-light:#dcdde0;
    --grey-dark:#4a4d52;
    --mark:#8d72ad;
  }
  *{box-sizing:border-box;margin:0;padding:0}
  html,body{width:1200px;height:1200px;overflow:hidden;background:var(--backdrop);font-family:"Raleway",sans-serif;color:var(--ink)}
  .canvas{position:relative;width:1200px;height:1200px}

  /* Cover */
  .cover{position:absolute;left:380px;top:40px;width:440px;height:440px;
    background:linear-gradient(160deg,var(--mint) 0%,var(--sky) 40%,var(--rose) 75%,var(--lilac) 100%);
    box-shadow:0 6px 18px rgba(0,0,0,.12);display:flex;flex-direction:column;align-items:center;justify-content:center}
  .cover-glow{position:absolute;inset:60px 110px 90px;border-radius:50%;
    background:radial-gradient(ellipse at center,rgba(255,255,255,.55),rgba(255,255,255,0) 70%)}
  .brand{display:flex;align-items:center;gap:8px;font-weight:400;color:var(--mark);position:relative}
  .brand-dot{border-radius:50%;background:var(--mark)}
  .cover .brand{font-size:34px;margin-top:70px}
  .cover .brand-dot{width:30px;height:30px}
  .cover-title{position:relative;margin-top:18px;font-size:13px;letter-spacing:3px;text-align:center;line-height:1.5;color:var(--ink)}

  /* Spread */
  .spread{position:absolute;left:60px;top:530px;width:1080px;height:620px;display:flex;box-shadow:0 8px 22px rgba(0,0,0,.12)}
  .page{position:relative;width:540px;height:620px;background:var(--paper);padding:44px 40px}
  .page-left{background:linear-gradient(90deg,#fff 88%,#ececec 100%)}
  .page-right{background:linear-gradient(270deg,#fff 88%,#ececec 100%)}
  .section-head{display:flex;align-items:center;height:40px;
    background:linear-gradient(90deg,var(--teal-pale),rgba(207,233,232,0));}
  .section-num{width:40px;height:40px;background:var(--teal);color:#fff;font-weight:600;font-size:16px;display:flex;align-items:center;justify-content:center}
  .section-title{margin-left:14px;font-size:19px;font-weight:500;letter-spacing:2px;color:var(--teal)}
  .section-intro{margin-top:16px;font-size:10px;line-height:1.5;color:var(--ink-soft);max-width:360px}

  .bg-grid{margin-top:22px;display:grid;grid-template-columns:repeat(3,140px);gap:16px;justify-content:center}
  .bg-tile{height:94px;display:flex;align-items:center;justify-content:center}
  .bg-tile .brand{font-size:15px;gap:5px}
  .bg-tile .brand-dot{width:13px;height:13px}
  .on-dark .brand{color:#e7dcf1}.on-dark .brand-dot{background:#e7dcf1}
  .t1{background:var(--plum-dark)}.t2{background:var(--plum)}.t3{background:var(--teal-dark)}
  .t4{background:var(--violet)}.t5{background:var(--pearl)}.t6{background:var(--green-light)}
  .t7{background:var(--grey-light)}.t8{background:var(--grey-dark)}.t9{background:#eef0f3}

  .misuse-grid{margin-top:20px;display:grid;grid-template-columns:repeat(3,140px);gap:14px 16px;justify-content:center}
  .misuse{display:flex;flex-direction:column;align-items:center}
  .misuse-box{width:140px;height:58px;display:flex;align-items:center;justify-content:center}
  .misuse-box .brand{font-size:15px;gap:5px;color:var(--ink)}
  .misuse-box .brand-dot{width:13px;height:13px;background:var(--ink)}
  .misuse-box.boxed{border:1px solid var(--ink-soft)}
  .misuse-box.tinted .brand{color:var(--teal)}.misuse-box.tinted .brand-dot{background:var(--teal)}
  .misuse-box.photo{background:linear-gradient(135deg,#8fa0b4,#c8ced6 60%,#7c8898)}
  .misuse-caption{margin-top:5px;font-size:9px;color:var(--ink-soft)}

  .page-foot{position:absolute;bottom:26px;font-size:8px;letter-spacing:2px;color:var(--ink-soft);text-transform:uppercase}
  .page-left .page-foot{left:40px}.page-right .page-foot{right:40px}
</style>
</head>
<body>
<main class="canvas">
  <section class="cover">
    <div class="cover-glow"></div>
    <div class="brand"><span class="brand-dot"></span>Verdalia</div>
    <p class="cover-title">MANUAL DE<br>IDENTIDADE VISUAL</p>
  </section>

  <section class="spread">
    <article class="page page-left">
      <header class="section-head"><span class="section-num">04</span><h2 class="section-title">APLICAÇÕES EM FUNDOS</h2></header>
      <p class="section-intro">Exemplos de aplicação da marca sobre fundos coloridos, mantendo sempre a legibilidade e o contraste adequado.</p>
      <div class="bg-grid">
        <div class="bg-tile t1 on-dark"><div class="brand"><span class="brand-dot"></span>Verdalia</div></div>
        <div class="bg-tile t2 on-dark"><div class="brand"><span class="brand-dot"></span>Verdalia</div></div>
        <div class="bg-tile t3 on-dark"><div class="brand"><span class="brand-dot"></span>Verdalia</div></div>
        <div class="bg-tile t4 on-dark"><div class="brand"><span class="brand-dot"></span>Verdalia</div></div>
        <div class="bg-tile t5"><div class="brand"><span class="brand-dot"></span>Verdalia</div></div>
        <div class="bg-tile t6"><div class="brand"><span class="brand-dot"></span>Verdalia</div></div>
        <div class="bg-tile t7"><div class="brand"><span class="brand-dot"></span>Verdalia</div></div>
        <div class="bg-tile t8 on-dark"><div class="brand"><span class="brand-dot"></span>Verdalia</div></div>
        <div class="bg-tile t9"><div class="brand"><span class="brand-dot"></span>Verdalia</div></div>
      </div>
      <footer class="page-foot">Manual de Identidade Visual</footer>
    </article>

    <article class="page page-right">
      <header class="section-head"><span class="section-num">05</span><h2 class="section-title">APLICAÇÕES INDEVIDAS</h2></header>
      <p class="section-intro">A marca não deve sofrer alterações de cor, proporção ou forma. Evite os usos abaixo.</p>
      <div class="misuse-grid">
        <div class="misuse"><div class="misuse-box"><div class="brand"><span class="brand-dot"></span>Verdalia</div></div><span class="misuse-caption">Não distorcer</span></div>
        <div class="misuse"><div class="misuse-box tinted"><div class="brand"><span class="brand-dot"></span>Verdalia</div></div><span class="misuse-caption">Não mudar cores</span></div>
        <div class="misuse"><div class="misuse-box"><div class="brand"><span class="brand-dot"></span>Verdalia</div></div><span class="misuse-caption">Não rotacionar</span></div>
        <div class="misuse"><div class="misuse-box boxed"><div class="brand"><span class="brand-dot"></span>Verdalia</div></div><span class="misuse-caption">Não usar contorno</span></div>
        <div class="misuse"><div class="misuse-box"><div class="brand"><span class="brand-dot"></span>Verdalia</div></div><span class="misuse-caption">Não aplicar sombra</span></div>
        <div class="misuse"><div class="misuse-box"><div class="brand"><span class="brand-dot"></span>Verdalia</div></div><span class="misuse-caption">Não alterar fonte</span></div>
        <div class="misuse"><div class="misuse-box"><div class="brand"><span class="brand-dot"></span>Verdalia</div></div><span class="misuse-caption">Não reduzir demais</span></div>
        <div class="misuse"><div class="misuse-box"><div class="brand"><span class="brand-dot"></span>Verdalia</div></div><span class="misuse-caption">Não espaçar</span></div>
        <div class="misuse"><div class="misuse-box tinted"><div class="brand"><span class="brand-dot"></span>Verdalia</div></div><span class="misuse-caption">Não inverter</span></div>
        <div class="misuse"><div class="misuse-box boxed"><div class="brand"><span class="brand-dot"></span>Verdalia</div></div><span class="misuse-caption">Não usar degradê</span></div>
        <div class="misuse"><div class="misuse-box photo" role="img" aria-label="Fotografia de fundo com a marca aplicada sobre ela"></div><span class="misuse-caption">Não usar em fotos</span></div>
        <div class="misuse"><div class="misuse-box"><div class="brand"><span class="brand-dot"></span>Verdalia</div></div><span class="misuse-caption">Não mudar proporção</span></div>
      </div>
      <footer class="page-foot">Manual de Identidade Visual</footer>
    </article>
  </section>
</main>
</body>
</html>
```